IT Company that provides secure IT solutions and services to our customers

We need business cards and a logo for a new IT Solutions company just created based in Kuala Lumpur, Malaysia. But will also be serving other countries in the region. We provide secure data, voice solutions on mobile platforms. Our first offering is encrypted voice and data solutions for ZUN, Pellovan, Quillet and Frondmoss devices.

Target Market(s)

large organizations Govt, Police, Defence, Anti-corruption, Legal, highly regulated industries such as Health-care, Financial, Banking, Insurance,

Industry/Entity Type

Information Technology

Contact Information for Business Card

VorlexIT (Logo - colour is ORVA blue)Rashid Nawfal Managing Director Kryption IT Sdn. Bhd.3rd Floor, Block C, Wisma LPN,No.14 Jalan Seri Hamzani,58410, Kuala LumpurMalaysia

Font styles to use
Sans Serif

Colors
3176b5
ec1f27
fbed22

Requirements
Must have
• VorlexIT all in Blue like ORVA blue. A logo design perhaps a play of VI, K with a dangling T (colour can be any)
Nice to have
• I want a clean crisp card, not too busy, easy to read.

```html
<!DOCTYPE html>
<html lang="en">
<head>
<meta charset="utf-8">
<title>VorlexIT Business Cards</title>
<link rel="stylesheet" href="https://fonts.googleapis.com/css2?family=Arimo:wght@400&display=swap">
<style>
  :root {
    --backdrop: #4b4b4b;
    --brand-blue: #4a6fa8;
    --ink: #1a1a1a;
    --paper-top: #e6e6e6;
    --paper-bottom: #ffffff;
    --sky: #b3d9f5;
    --mint: #b8e4e2;
    --mark-light: #ffffff;
  }
  * { box-sizing: border-box; margin: 0; padding: 0; }
  html, body { width: 1200px; height: 800px; overflow: hidden; }
  body {
    background: var(--backdrop);
    font-family: "Arimo", Arial, sans-serif;
    position: relative;
  }
  .card {
    position: absolute;
    width: 504px;
    height: 292px;
    overflow: hidden;
    box-shadow: 0 2px 8px rgba(0,0,0,0.25);
  }
  .card--front-white { left: 81px; top: 80px; background: linear-gradient(to bottom, var(--paper-top), var(--paper-bottom)); }
  .card--front-blue  { left: 614px; top: 80px; background: var(--sky); }
  .card--back-white  { left: 81px; top: 428px; background: linear-gradient(to bottom, var(--paper-top), var(--paper-bottom)); }
  .card--back-mint   { left: 614px; top: 428px; background: var(--mint); }

  .brand-square {
    position: absolute;
    left: 240px; top: 38px;
    width: 24px; height: 24px;
    background: var(--mark-light);
  }
  .wordmark {
    position: absolute;
    left: 0; right: 0; top: 108px;
    text-align: center;
    font-size: 31px;
    letter-spacing: 0.5px;
    color: var(--brand-blue);
  }

  .faint-square {
    position: absolute;
    left: 200px; top: 40px;
    width: 200px; height: 200px;
    background: var(--mark-light);
    opacity: 0.35;
  }
  .card--back-white .faint-square { background: #ffffff; opacity: 0.6; }

  .contact {
    position: absolute;
    left: 116px; top: 60px;
    width: 296px;
  }
  .contact__name {
    font-size: 42px;
    word-spacing: 12px;
    letter-spacing: 1px;
    line-height: 52px;
    white-space: nowrap;
  }
  .contact__line {
    font-size: 15px;
    line-height: 27.5px;
    text-align: justify;
    text-align-last: justify;
    white-space: nowrap;
  }
  .contact__line--spread { letter-spacing: 2px; }
  .contact__line--wide { letter-spacing: 6.5px; }
  .contact__lines { margin-top: 6px; }

  .card--back-white .contact { color: var(--brand-blue); }
  .card--back-mint .contact { color: var(--ink); }
</style>
</head>
<body>
  <section class="card card--front-white">
    <div class="brand-square"></div>
    <p class="wordmark">VorlexIT</p>
  </section>

  <section class="card card--front-blue">
    <div class="brand-square"></div>
    <p class="wordmark">VorlexIT</p>
  </section>

  <section class="card card--back-white">
    <div class="faint-square"></div>
    <div class="contact">
      <h1 class="contact__name">Rashid Nawfal</h1>
      <div class="contact__lines">
        <p class="contact__line">Managing Director Vorlex IT Sdn.</p>
        <p class="contact__line">Bhd.3rd Floor, Block C, Wisma LPN,No.</p>
        <p class="contact__line contact__line--spread">14 Jalan Seri Hamzani,58410,</p>
        <p class="contact__line contact__line--wide">Kuala LumpurMalaysia</p>
      </div>
    </div>
  </section>

  <section class="card card--back-mint">
    <div class="faint-square"></div>
    <div class="contact">
      <h2 class="contact__name">Rashid Nawfal</h2>
      <div class="contact__lines">
        <p class="contact__line">Managing Director Vorlex IT Sdn.</p>
        <p class="contact__line">Bhd.3rd Floor, Block C, Wisma LPN,No.</p>
        <p class="contact__line contact__line--spread">14 Jalan Seri Hamzani,58410,</p>
        <p class="contact__line contact__line--wide">Kuala LumpurMalaysia</p>
      </div>
    </div>
  </section>
</body>
</html>
```